Tomas Whitlow Design, LLC (www.tomaswhitlow.design)

A very hip, trendy architectural home page. Simple Menu upper right hand corner (About, Projects, Inspiration, Design-Build, Contact). In the "Projects" ... I want to click on each project and that will open up multiple photo's of that project. Attached are the graphics of my logo. I want the home page to be incredible ... I really market my name "Tomas Whitlow" as sophisticated architecture. Colors/branding should be black/metallic/white/grey maybe with a pop of a bright color but not much. My architecture is like www.brennerfaulkatelier.com if you want to review as example. My specialty is industrial design, homes with architectural concrete design, steel beams, alot of glass. Very modern. My work is best illustrated at www.vasquerlind.com.
Updates

Please see images uploaded in my brief. A new business card design by an AWESOME designer and some inspirational architectural projects I worked on.

Industry/Entity Type

Architecture

Coding

Coded - Design and coding required

Number of Pages Required

5+ page

Colors

Designer to choose only greyscale colors for use in the design.

Requirements
Must have
• The 1st project photo gallery is called "Raw Dwelling at Cypress Point"... Images of this project can be taken from: https://www.homeplotra.com/homedetails/2817-9th-St-SE-Naples-FL-34117/508164229_zpid/

The 2nd project photo gallery is called "Stone, Iron and Timber Residence at Cypress Point". I will upload images for this project but use placeholder until I finalize.

The 3rd photo gallery is called "Early Sketches: Off the Page". I will forward pictures. for this.

Website should be easy to update and handover at completion as we will be updating frequently. Wordpress, WIX, or other type is fine as long as it looks profesional and high-class.
Nice to have
• Maybe the home page loads to just "Tomas Whitlow Design, LLC ... Atelier for Bold Structural Vision" and has a click to enter button. Something cool maybe a fade it or something eye-catching and cool.
Should not have
• Should not be overly colorful.

```html
<!DOCTYPE html>
<html lang="en">
<head>
<meta charset="UTF-8">
<title>Tomas Whitlow Design, LLC — Home</title>
<link rel="stylesheet" href="https://fonts.googleapis.com/css2?family=Playfair+Display:wght@700&family=Poppins:wght@300;400&display=swap">
<style>
  :root {
    --bg: #1a1d21;
    --page: #1b1e23;
    --white: #ffffff;
    --soft-white: #e9eaec;
    --grey: #8a8d92;
    --rule: #4a4d52;
    --dot: #6d7075;
    --photo-dark: #1c1f22;
    --photo-mid: #4b4f55;
    --photo-sky: #8a8e96;
  }
  * { box-sizing: border-box; margin: 0; padding: 0; }
  html, body { width: 1200px; height: 1000px; overflow: hidden; background: var(--bg); }
  body { position: relative; font-family: "Poppins", sans-serif; color: var(--white); }

  /* Brand lockup */
  .brand-lockup {
    position: absolute; top: 70px; left: 0; width: 1200px;
    display: flex; justify-content: center; align-items: center; gap: 34px;
  }
  .brand-mark { width: 92px; height: 92px; border: 6px solid var(--white); }
  .brand-name { font-weight: 300; color: var(--white); line-height: 1.1; }
  .brand-name .name-main { display: block; font-size: 58px; letter-spacing: 1px; }
  .brand-name .name-sub { display: block; font-size: 22px; letter-spacing: 9px; text-align: center; margin-top: 8px; }

  /* Website home page */
  .site {
    position: absolute; left: 100px; top: 290px; width: 1000px; height: 563px;
    background: var(--page); overflow: hidden; outline: 1px solid #24272c;
  }
  .site-nav {
    position: absolute; left: 0; top: 0; width: 100%; height: 66px;
    border-bottom: 1px solid var(--rule);
    display: flex; align-items: center; justify-content: space-between;
    padding: 0 51px;
  }
  .nav-brand { display: flex; align-items: center; gap: 10px; }
  .nav-brand-mark { width: 24px; height: 24px; border: 2px solid var(--soft-white); }
  .nav-brand-name { font-weight: 300; font-size: 13px; color: var(--soft-white); letter-spacing: .5px; }
  .nav-menu { display: flex; gap: 38px; list-style: none; }
  .nav-menu li { font-size: 12.5px; font-weight: 400; color: var(--soft-white); }

  .hero-photo {
    position: absolute; left: 442px; top: 101px; width: 558px; height: 357px;
    background:
      linear-gradient(180deg, transparent 0%, transparent 55%, rgba(20,22,24,.9) 100%),
      linear-gradient(180deg, var(--photo-sky) 0%, var(--photo-mid) 45%, var(--photo-dark) 100%);
  }
  .hero-dots { position: absolute; left: 414px; top: 374px; }

  .hero-year {
    position: absolute; left: 51px; top: 146px;
    font-size: 38px; font-weight: 300; letter-spacing: -1px;
    color: transparent; -webkit-text-stroke: 1px var(--grey);
  }
  .hero-title {
    position: absolute; left: 51px; top: 198px; z-index: 2;
    font-family: "Playfair Display", serif; font-weight: 700;
    font-size: 55px; line-height: 79px; color: var(--white);
  }
  .hero-button {
    position: absolute; left: 51px; top: 377px;
    width: 123px; height: 38px; border: 1.5px solid var(--soft-white); border-radius: 2px;
    display: flex; align-items: center; justify-content: center;
    font-size: 13px; font-weight: 400; color: var(--soft-white);
  }
  .scroll-progress {
    position: absolute; left: 0; bottom: 1px; width: 285px; height: 2px; background: #3a3d42;
  }
</style>
</head>
<body>
  <header class="brand-lockup">
    <div class="brand-mark"></div>
    <div class="brand-name">
      <span class="name-main">Tomas Whitlow</span>
      <span class="name-sub">DESIGN, LLC</span>
    </div>
  </header>

  <main class="site">
    <nav class="site-nav">
      <div class="nav-brand">
        <div class="nav-brand-mark"></div>
        <span class="nav-brand-name">Tomas Whitlow Design, LLC</span>
      </div>
      <ul class="nav-menu">
        <li>Home</li>
        <li>About</li>
        <li>Projects</li>
        <li>Inspiration</li>
        <li>Design-build</li>
        <li>Contact</li>
      </ul>
    </nav>

    <svg class="hero-dots" width="130" height="110" viewBox="0 0 130 110" aria-hidden="true">
      <g fill="var(--dot)">
        <circle cx="3" cy="3" r="2"/><circle cx="20" cy="3" r="2"/>
        <circle cx="3" cy="20" r="2"/><circle cx="20" cy="20" r="2"/>
        <circle cx="3" cy="37" r="2"/><circle cx="20" cy="37" r="2"/>
        <circle cx="3" cy="54" r="2"/><circle cx="20" cy="54" r="2"/>
        <circle cx="3" cy="71" r="2"/><circle cx="20" cy="71" r="2"/>
        <circle cx="3" cy="88" r="2"/><circle cx="20" cy="88" r="2"/><circle cx="37" cy="88" r="2"/><circle cx="54" cy="88" r="2"/><circle cx="71" cy="88" r="2"/><circle cx="88" cy="88" r="2"/><circle cx="105" cy="88" r="2"/><circle cx="122" cy="88" r="2"/>
        <circle cx="3" cy="105" r="2"/><circle cx="20" cy="105" r="2"/><circle cx="37" cy="105" r="2"/><circle cx="54" cy="105" r="2"/><circle cx="71" cy="105" r="2"/><circle cx="88" cy="105" r="2"/><circle cx="105" cy="105" r="2"/><circle cx="122" cy="105" r="2"/>
      </g>
    </svg>

    <div class="hero-photo" role="img" aria-label="Photograph of a modern concrete, steel and glass house lit at dusk, set among tall pine trees with grasses in front"></div>

    <p class="hero-year">/2021</p>
    <h1 class="hero-title">Atelier for Bold<br>Structural Vision.</h1>
    <div class="hero-button">About</div>
    <div class="scroll-progress"></div>
  </main>
</body>
</html>
```